Corporate Design für die Alta Marea! GmbH
Zielgruppe
Die Alta Marea! GmbH begibt sich auf den Weg mit den Firmen, die sie gründet, kauft, entwickelt und verkauft. Wir sind eine Holding, beteiligen uns an Firmen oder gründen diese neu. 'Alta Marea!' ist der Pilgergruß auf dem Jakobsweg - diesen bin ich schon 5 Mal gegangen und die Metapher 'Gründen als Weg/Pilgerreise' finde ich sehr zutreffend. Ferner gibt es einen gelben Pfeil auf dem Jakobsweg, der einen immer verfolgt und einem den Weg weist. Das sind wir auch.
Aufgabenstellung
Es ist am Ende das Tages eine Holding, bei der sich Gründer und Firmen melden sollen, weil sie Beratung oder Kapital brauchen - daher ist Seriosität zwar unbedingt notwendig aber sie soll nicht abschrecken, elitär, 'Anwalt-grau-blau-weiß-bieder' sein. Gründertum, Unternehmertum, Freude, Machen, Erfolg!
Pilgern macht Freude und Gründen und Firmen haben auch. Mit uns um so mehr! Ein toller Weg!
'Alta Marea!' eben
Wir heißen 'Alta Marea! GmbH' - mit einem Ausrufezeichen angemeldet und das ist wichtig. Wir haben keine 'Fragezeichen' oder 'Punkte' wir haben ein Ausrufezeichen und einen Pfeil, ein Ziel, einen Weg, Etappen...
Die Abkürzung 'AM!' kann eine Möglichkeit sein aber ausgeschrieben wäre mir lieber - AM! kann das Favicon oder eine Logo-Kurzform/Variante sein

```html
<!DOCTYPE html>
<html lang="de">
<head>
<meta charset="utf-8">
<title>Alta Marea! – Corporate Design</title>
<link href="https://fonts.googleapis.com/css2?family=Roboto+Condensed:wght@700&family=Nunito+Sans:wght@400;600&display=swap" rel="stylesheet">
<style>
:root{
  --grey:#878787;
  --grey-light:#cfcfcf;
  --grey-faint:#efefef;
  --yellow:#fcc200;
  --blue:#5b8bd2;
  --white:#ffffff;
  --bg:#ffffff;
}
*{margin:0;padding:0;box-sizing:border-box}
html,body{width:1200px;height:4454px;overflow:hidden;background:var(--bg)}
body{position:relative;font-family:"Nunito Sans",sans-serif;color:var(--grey)}
.abs{position:absolute}
.wordmark{font-family:"Roboto Condensed",sans-serif;font-weight:700;color:var(--grey);white-space:nowrap;line-height:1;display:flex;align-items:center}
.wordmark .dot{display:inline-block;border-radius:50%;background:var(--yellow);margin-left:.18em}
.wordmark.light{color:var(--white)}
.sheet{background:var(--white);box-shadow:4px 6px 14px rgba(0,0,0,.22)}
.blue-top{position:absolute;left:0;top:0;right:0;background:var(--blue)}
.grey-bottom{position:absolute;left:0;bottom:0;right:0;background:var(--grey)}
.contact{font-size:15px;line-height:21px}
.contact li{list-style:none;display:flex;align-items:center;gap:8px}
.contact svg{width:12px;height:12px;fill:var(--grey)}
.faint-circle{position:absolute;border-radius:50%;background:var(--grey-faint)}
.mark{position:absolute;width:16px;height:16px;border-color:var(--grey);border-style:solid;border-width:0}
.fold{position:absolute;left:0;width:12px;height:2px;background:var(--grey)}
.footer{position:absolute;left:0;right:0;bottom:0;height:89px;background:var(--grey);color:var(--white);font-size:13.5px;line-height:18px;display:flex;padding-top:14px}
.footer .col{border-left:2px solid var(--white);padding-left:8px;position:absolute;top:14px}
.card-name{font-size:16px;font-weight:600;line-height:17px}
.card-role{font-size:12px}
.card-addr{font-size:11.5px;line-height:15px}
.card-contact{font-size:12px;line-height:18px}
.card-contact li{list-style:none;display:flex;align-items:center;gap:9px}
.card-contact svg{width:10px;height:10px}
.frame{position:absolute;border:6px solid var(--grey)}
</style>
</head>
<body>

<!-- Primary wordmark -->
<div class="wordmark abs" style="left:62px;top:118px;font-size:146px;letter-spacing:1px">ALTA MAREA!<span class="dot" style="width:40px;height:40px"></span></div>

<!-- Short-form variants -->
<div class="frame" style="left:65px;top:552px;width:264px;height:264px"></div>
<div class="abs" style="left:118px;top:790px;width:158px;height:30px;background:var(--white)"></div>
<div class="wordmark abs" style="left:127px;top:725px;font-size:104px">AM!</div>

<div class="frame" style="left:473px;top:552px;width:264px;height:264px"></div>
<div class="abs" style="left:580px;top:700px;width:170px;height:120px;background:var(--white)"></div>
<div class="wordmark abs" style="left:590px;top:700px;font-size:130px">AM!</div>

<div class="wordmark abs" style="left:900px;top:700px;font-size:130px">AM!</div>
<div class="abs" style="left:940px;top:570px;width:70px;height:70px;border-radius:50%;background:var(--yellow)"></div>

<!-- Letterhead -->
<section class="sheet abs" style="left:82px;top:948px;width:1001px;height:1414px">
  <div class="blue-top" style="height:11px"></div>
  <div class="wordmark abs" style="right:50px;top:116px;font-size:42px">ALTA MAREA!<span class="dot" style="width:12px;height:12px"></span></div>
  <p class="abs" style="left:119px;top:219px;font-size:12.5px">Alta Marea! GmbH | Musterstrasse 123 | 12345 Musterstadt</p>
  <span class="mark" style="left:107px;top:212px;border-left-width:2px;border-top-width:2px"></span>
  <span class="mark" style="left:497px;top:212px;border-right-width:2px;border-top-width:2px"></span>
  <span class="mark" style="left:107px;top:413px;border-left-width:2px;border-bottom-width:2px"></span>
  <span class="mark" style="left:497px;top:413px;border-right-width:2px;border-bottom-width:2px"></span>
  <ul class="contact abs" style="left:758px;top:218px">
    <li><svg viewBox="0 0 12 12"><path d="M2 1l2 0 1 3-1.5 1a6 6 0 003 3L8 7l3 1v2l-1 1C5 11 1 7 1 2z"/></svg>+41 123 / 45 67 89 01</li>
    <li><svg viewBox="0 0 12 12"><rect x="1" y="5" width="10" height="5"/><rect x="3" y="1" width="6" height="4"/></svg>+41 123 / 45 67 89 01</li>
    <li><svg viewBox="0 0 12 12"><rect x="1" y="2" width="10" height="8"/></svg>info@alta-marea.de</li>
    <li><svg viewBox="0 0 12 12"><circle cx="6" cy="6" r="5"/></svg>www.alta-marea.de</li>
  </ul>
  <span class="fold" style="top:496px"></span>
  <span class="fold" style="top:994px"></span>
  <div class="faint-circle" style="left:330px;top:570px;width:330px;height:330px"></div>
  <div class="abs" style="left:0;right:0;bottom:92px;height:4px;background:var(--yellow)"></div>
  <div class="footer">
    <div class="col" style="left:94px">Musterstrasse 123<br>12345 Musterstadt<br>Geschäftsführung Max Muster</div>
    <div class="col" style="left:375px">Bankverbindung<br>BIC: &nbsp;ABCDEFGHXXX<br>IBAN: DE 00 0000 0000 0000 0000 00</div>
    <div class="col" style="left:750px">Finanzamt<br>Musterstadt<br>USt-IdNr.: DE000000000</div>
  </div>
</section>

<!-- Business card 1 front -->
<section class="sheet abs" style="left:96px;top:2444px;width:475px;height:307px;background:var(--grey);overflow:hidden">
  <div class="faint-circle" style="left:250px;top:40px;width:300px;height:300px;background:rgba(255,255,255,.06)"></div>
  <div class="wordmark light abs" style="left:82px;top:125px;font-size:50px">ALTA MAREA!<span class="dot" style="width:14px;height:14px"></span></div>
</section>
<!-- Business card 1 back -->
<section class="sheet abs" style="left:619px;top:2444px;width:475px;height:307px;overflow:hidden">
  <div class="abs" style="left:238px;top:0;width:237px;height:307px;background:var(--grey)"></div>
  <div class="wordmark light abs" style="right:16px;top:60px;font-size:32px">ALTA MAREA!<span class="dot" style="width:9px;height:9px"></span></div>
  <p class="card-name abs" style="left:13px;top:172px">MAX MUSTER</p>
  <p class="card-role abs" style="left:13px;top:189px">Geschäftsführer</p>
  <p class="card-addr abs" style="left:13px;top:268px">Musterstrasse 123<br>12345 Musterstadt</p>
  <ul class="card-contact abs" style="left:262px;top:205px;color:var(--white)">
    <li><svg viewBox="0 0 12 12" fill="#fff"><path d="M2 1l2 0 1 3-1.5 1a6 6 0 003 3L8 7l3 1v2l-1 1C5 11 1 7 1 2z"/></svg>+41 123 / 45 67 89 01</li>
    <li><svg viewBox="0 0 12 12" fill="#fff"><rect x="1" y="5" width="10" height="5"/></svg>+41 123 / 45 67 89 01</li>
    <li><svg viewBox="0 0 12 12" fill="#fff"><rect x="3" y="1" width="6" height="10" rx="1"/></svg>+41 123 / 45 67 89 01</li>
    <li><svg viewBox="0 0 12 12" fill="#fff"><rect x="1" y="2" width="10" height="8"/></svg>info@alta-marea.de</li>
    <li><svg viewBox="0 0 12 12" fill="#fff"><circle cx="6" cy="6" r="5"/></svg>www.alta-marea.de</li>
  </ul>
</section>

<!-- Business card 2 front -->
<section class="sheet abs" style="left:96px;top:2825px;width:475px;height:305px;overflow:hidden">
  <div class="blue-top" style="height:10px"></div>
  <div class="grey-bottom" style="height:10px"></div>
  <div class="faint-circle" style="left:250px;top:40px;width:300px;height:300px"></div>
  <div class="wordmark abs" style="left:82px;top:125px;font-size:50px">ALTA MAREA!<span class="dot" style="width:14px;height:14px"></span></div>
</section>
<!-- Business card 2 back -->
<section class="sheet abs" style="left:619px;top:2825px;width:475px;height:305px;overflow:hidden">
  <div class="blue-top" style="height:10px"></div>
  <div class="grey-bottom" style="height:10px"></div>
  <div class="wordmark abs" style="right:16px;top:68px;font-size:32px">ALTA MAREA!<span class="dot" style="width:9px;height:9px"></span></div>
  <p class="card-name abs" style="left:13px;top:167px">MAX MUSTER</p>
  <p class="card-role abs" style="left:13px;top:184px">Geschäftsführer</p>
  <p class="card-addr abs" style="left:13px;top:257px">Musterstrasse 123<br>12345 Musterstadt</p>
  <ul class="card-contact abs" style="left:300px;top:200px">
    <li><svg viewBox="0 0 12 12" fill="#878787"><path d="M2 1l2 0 1 3-1.5 1a6 6 0 003 3L8 7l3 1v2l-1 1C5 11 1 7 1 2z"/></svg>+41 123 / 45 67 89 01</li>
    <li><svg viewBox="0 0 12 12" fill="#878787"><rect x="1" y="5" width="10" height="5"/></svg>+41 123 / 45 67 89 01</li>
    <li><svg viewBox="0 0 12 12" fill="#878787"><rect x="3" y="1" width="6" height="10" rx="1"/></svg>+41 123 / 45 67 89 01</li>
    <li><svg viewBox="0 0 12 12" fill="#878787"><rect x="1" y="2" width="10" height="8"/></svg>info@alta-marea.de</li>
    <li><svg viewBox="0 0 12 12" fill="#878787"><circle cx="6" cy="6" r="5"/></svg>www.alta-marea.de</li>
  </ul>
</section>

<!-- Envelope front -->
<section class="sheet abs" style="left:89px;top:3245px;width:1011px;height:504px">
  <div class="blue-top" style="height:11px"></div>
  <div class="grey-bottom" style="height:11px"></div>
  <div class="wordmark abs" style="left:170px;top:165px;font-size:40px">ALTA MAREA!<span class="dot" style="width:11px;height:11px"></span></div>
  <div class="abs" style="left:89px;top:243px;width:395px;height:194px;border-radius:22px;background:var(--grey-light)"></div>
</section>

<!-- Envelope back -->
<section class="sheet abs" style="left:89px;top:3821px;width:1011px;height:502px">
  <svg class="abs" style="left:0;top:0" width="1011" height="145" viewBox="0 0 1011 145">
    <path d="M0 0H1011L964 130Q959 144 944 144H67Q52 144 47 130Z" fill="#5b8bd2"/>
  </svg>
  <div class="wordmark light abs" style="left:387px;top:49px;font-size:40px">ALTA MAREA!<span class="dot" style="width:11px;height:11px"></span></div>
  <div class="grey-bottom" style="height:11px"></div>
</section>

</body>
</html>
```